Web Calculator design Housing Investment

We have a web calculator that needs to be fixed from a design perspective. The key tasks are:<br/>1. Selecting icons / pictures / colours for the various steps<br/>2. Designing navigation between calculator steps<br/>3. Making suggestions for chart design. The limitation is that the charts are all using the Plovik API (the same charts that Plovik Grids use).<br/><br/>There are four entry screens and then a result screen. See attached PDF for screenshots. You can see our website at https://ambertidefunds.com for our corporate colours and style.

Target Market(s)

Real Estate Investors

Industry/Entity Type

Financial Planning

Number of Pages Required

1 page

Font styles to use
Sans Serif
Other font styles liked:
• Ubuntu

Colors
86cae7
3176b5
0455a3
ffffff

Requirements
Must have
• New Icons
• Suggested design for navigation
• Suggested design for charts

```html
<!DOCTYPE html>
<html lang="en">
<head>
<meta charset="utf-8">
<title>Housing Investment Calculator – Step Designs</title>
<link href="https://fonts.googleapis.com/css2?family=Source+Sans+3:wght@400;600;700&display=swap" rel="stylesheet">
<style>
:root{
  --navy:#0455a3;
  --mid:#3176b5;
  --sky:#86cae7;
  --map:#0aa9e8;
  --white:#ffffff;
  --ink:#4a4a4a;
  --soft:#8a8a8a;
  --band:#eeeeee;
  --grey-btn:#d9d9d9;
  --rule:#e3e3e3;
  --accent:#e2701f;
  --rose:#e8505b;
  --pink:#e0399a;
}
*{box-sizing:border-box;margin:0;padding:0}
html,body{width:1200px;height:2432px;overflow:hidden;background:var(--white)}
body{font-family:"Source Sans 3",Arial,sans-serif;color:var(--ink)}
.board{position:absolute;left:0;top:0;width:1275px;height:2584px;transform:scale(.9412);transform-origin:0 0}
.panel{position:absolute;left:160px;width:950px;background:var(--white);box-shadow:0 0 6px rgba(0,0,0,.22)}
.stepper{position:absolute;left:5px;right:5px;top:14px;height:32px;background:var(--band)}
.step{position:absolute;top:0;height:32px}
.step .mark{position:absolute;top:2px;width:28px;height:28px;left:-14px}
.step .mark::before{content:"";position:absolute;inset:4px;transform:rotate(45deg);background:var(--white);border:1.5px solid var(--navy);border-radius:2px}
.step.active .mark::before{background:var(--navy)}
.step .num{position:absolute;left:0;top:0;width:28px;height:28px;line-height:28px;text-align:center;font-size:12px;font-weight:600;color:var(--navy)}
.step.active .num{color:var(--white)}
.step .tick{position:absolute;left:8px;top:8px;width:12px;height:12px}
.step .label{position:absolute;top:7px;left:29px;font-size:13px;color:var(--soft);white-space:nowrap}
.step.active .label{color:#333}
.btn{position:absolute;height:36px;border-radius:18px;font-size:13px;font-weight:700;text-align:center;line-height:36px;letter-spacing:.3px}
.btn.next{width:95px;left:827px;background:var(--navy);color:var(--white)}
.btn.prev{width:107px;left:709px;background:var(--grey-btn);color:var(--navy)}
.question{position:absolute;left:0;right:0;text-align:center;font-size:12.5px;color:var(--ink)}
.choice{position:absolute;width:183px;height:173px;border-radius:22px;color:var(--white);text-align:center}
.choice.dark{background:var(--navy)}
.choice.light{background:var(--mid)}
.choice .name{font-size:15px;font-weight:600}
.choice .desc{position:absolute;left:10px;right:10px;top:128px;font-size:10.5px;line-height:15px}
.slider-row{position:absolute;left:425px;width:380px;font-size:10.5px;color:var(--ink)}
.slider-row .val{position:absolute;right:0;top:0}
.track{position:absolute;height:2px;background:var(--rule)}
.track .fill{position:absolute;left:0;top:0;height:2px;background:var(--navy)}
.knob{position:absolute;width:11px;height:11px;border:2px solid var(--navy);border-radius:50%;background:var(--white);top:-5px;margin-left:-5px}
.map-area{position:absolute;background:linear-gradient(160deg,#2fc0f3,var(--map));border-radius:40% 35% 45% 40%}
.select{position:absolute;height:26px;border:1px solid #cfcfcf;border-radius:2px;font-size:11px;color:#555;padding:6px 7px;background:var(--white)}
.select svg{position:absolute;right:7px;top:9px}
.line-text{position:absolute;font-size:11.5px;color:var(--ink);white-space:nowrap}
.card{position:absolute;top:127px;height:147px;border:1px solid #dcdcdc;background:var(--white)}
.small{font-size:10.5px;color:#666}
.result{text-align:center;color:#555}
.result .head{font-size:12px;font-weight:600;color:#555}
.result .sub{font-size:9.5px;color:#777}
.note{position:absolute;left:0;right:0;top:306px;text-align:center;font-size:9px;color:#9a9a9a}
.advanced{position:absolute;left:11px;width:929px;top:341px;height:33px;background:#f3f3f3;font-size:9.5px;color:#555;padding:10px 9px}
</style>
</head>
<body>
<div class="board">

<!-- Step 1: property type -->
<section class="panel" style="top:143px;height:354px">
  <div class="stepper">
    <div class="step active" style="left:33px"><div class="mark"><span class="num" style="left:0">1</span></div><span class="label">Property Type</span></div>
    <div class="step" style="left:219px"><div class="mark"><span class="num">2</span></div><span class="label">Property Location</span></div>
    <div class="step" style="left:413px"><div class="mark"><span class="num">3</span></div><span class="label">Property Valuation</span></div>
    <div class="step" style="left:598px"><div class="mark"><span class="num">4</span></div><span class="label">Your Property Forecast</span></div>
    <div class="step" style="left:825px"><div class="mark"><span class="num">5</span></div><span class="label">Calculation</span></div>
  </div>
  <div class="question" style="top:83px">What type of property would you like to compare?</div>
  <div class="btn next" style="top:74px">NEXT</div>
  <div class="choice dark" style="left:286px;top:122px">
    <svg width="76" height="76" viewBox="0 0 76 76" style="margin-top:34px" fill="none" stroke="#fff" stroke-width="1.6">
      <rect x="10" y="4" width="30" height="66"/><rect x="36" y="24" width="26" height="46"/>
      <path d="M2 70h72"/>
      <g stroke-width="1.3"><path d="M15 10v50M21 10v50M27 10v50M33 10v50" stroke-dasharray="3 3"/><path d="M42 30v34M48 30v34M55 30v34" stroke-dasharray="3 3"/></g>
      <path d="M40 70c2-6 10-6 12 0M54 70c2-5 8-5 10 0"/>
    </svg>
    <div class="name" style="margin-top:4px">Unit</div>
  </div>
  <div class="choice light" style="left:482px;top:122px">
    <svg width="76" height="76" viewBox="0 0 76 76" style="margin-top:34px" fill="none" stroke="#fff" stroke-width="1.6">
      <rect x="18" y="6" width="30" height="64"/><rect x="48" y="24" width="20" height="46"/>
      <path d="M23 12h8v8h-8zM35 12h8v8h-8zM23 26h8v8h-8zM35 26h8v8h-8zM23 40h8v8h-8zM35 40h8v8h-8zM53 30h10v8H53zM53 44h10v8H53zM28 56h10v14H28z"/>
      <path d="M12 70V50M12 50c-8-4-6-16 0-20 6 4 8 16 0 20zM12 60l-4-4M12 56l4-4"/>
      <path d="M4 70h70"/>
    </svg>
    <div class="name" style="margin-top:4px">House</div>
  </div>
</section>

<!-- Step 2: location -->
<section class="panel" style="top:595px;height:353px">
  <div class="stepper">
    <div class="step" style="left:33px"><div class="mark"><svg class="tick" viewBox="0 0 12 12"><path d="M2 6.5l2.6 2.6L10 3.5" fill="none" stroke="#0455a3" stroke-width="2"/></svg></div><span class="label">Property Type</span></div>
    <div class="step active" style="left:219px"><div class="mark"><span class="num">2</span></div><span class="label">Property Location</span></div>
    <div class="step" style="left:413px"><div class="mark"><span class="num">3</span></div><span class="label">Property Valuation</span></div>
    <div class="step" style="left:598px"><div class="mark"><span class="num">4</span></div><span class="label">Your Property Forecast</span></div>
    <div class="step" style="left:825px"><div class="mark"><span class="num">5</span></div><span class="label">Calculation</span></div>
  </div>
  <div class="question" style="top:83px">Where would this property be located?</div>
  <div class="btn prev" style="top:74px">PREVIOUS</div>
  <div class="btn next" style="top:74px">NEXT</div>
  <div class="map-area" role="img" aria-label="Map of Australia with selectable states" style="left:160px;top:113px;width:236px;height:219px"></div>
  <div class="slider-row" style="top:149px">How Much will The Property cost?<span class="val">$500,000</span></div>
  <div class="track" style="left:425px;width:380px;top:178px"><div class="fill" style="width:65px"></div><div class="knob" style="left:65px"></div></div>
  <div class="slider-row" style="top:202px">How Much will you invest?<span class="val">$200,000</span></div>
  <div class="track" style="left:425px;width:380px;top:231px"><div class="fill" style="width:20px"></div><div class="knob" style="left:20px"></div></div>
</section>

<!-- Step 3: valuation -->
<section class="panel" style="top:1033px;height:354px">
  <div class="stepper">
    <div class="step" style="left:33px"><div class="mark"><svg class="tick" viewBox="0 0 12 12"><path d="M2 6.5l2.6 2.6L10 3.5" fill="none" stroke="#0455a3" stroke-width="2"/></svg></div><span class="label">Property Type</span></div>
    <div class="step" style="left:219px"><div class="mark"><svg class="tick" viewBox="0 0 12 12"><path d="M2 6.5l2.6 2.6L10 3.5" fill="none" stroke="#0455a3" stroke-width="2"/></svg></div><span class="label">Property Location</span></div>
    <div class="step active" style="left:413px"><div class="mark"><span class="num">3</span></div><span class="label">Property Valuation</span></div>
    <div class="step" style="left:598px"><div class="mark"><span class="num">4</span></div><span class="label">Your Property Forecast</span></div>
    <div class="step" style="left:825px"><div class="mark"><span class="num">5</span></div><span class="label">Calculation</span></div>
  </div>
  <div class="question" style="top:84px">How would you like to forecast the returns from Property?</div>
  <div class="btn prev" style="top:75px">PREVIOUS</div>
  <div class="btn next" style="top:75px">NEXT</div>
  <div class="choice dark" style="left:188px;top:124px">
    <div class="name" style="margin-top:10px">Relative Cost</div>
    <svg width="76" height="64" viewBox="0 0 76 64" style="margin-top:6px" fill="none" stroke="#fff" stroke-width="1.8">
      <path d="M38 4v50M24 58h28M30 54h16M10 12h56M38 8c-6 0-8 4-28 4M38 8c6 0 8 4 28 4"/>
      <path d="M10 12L2 32h16zM2 32c0 8 16 8 16 0M66 12l-8 20h16zM58 32c0 8 16 8 16 0"/>
    </svg>
    <div class="desc">Use This to value property based on mortgage cost relative to rent cost</div>
  </div>
  <div class="choice light" style="left:384px;top:124px">
    <div class="name" style="margin-top:10px">Relative to Wages</div>
    <svg width="76" height="64" viewBox="0 0 76 64" style="margin-top:6px" fill="none" stroke="#fff" stroke-width="1.8">
      <circle cx="28" cy="22" r="17"/><path d="M32 15c-3-3-10-2-10 2 0 5 10 3 10 8 0 4-7 5-10 2M27 10v24"/>
      <circle cx="46" cy="26" r="8"/><path d="M30 62c0-12 6-20 16-20s16 8 16 20M46 42v14M40 48l6 4 6-4"/>
    </svg>
    <div class="desc">Use This to value property based on mortgage cost relative to Wages</div>
  </div>
  <div class="choice dark" style="left:580px;top:124px">
    <div class="name" style="margin-top:10px">Using Rental Yield</div>
    <svg width="76" height="64" viewBox="0 0 76 64" style="margin-top:6px" fill="none" stroke="#fff" stroke-width="1.8">
      <rect x="4" y="6" width="56" height="30" rx="2"/><rect x="8" y="10" width="48" height="22"/><ellipse cx="32" cy="21" rx="8" ry="6"/>
      <circle cx="52" cy="42" r="16" fill="#0455a3"/><path d="M45 49l14-14"/><circle cx="47" cy="37" r="2.5"/><circle cx="57" cy="47" r="2.5"/>
    </svg>
    <div class="desc">Use This to value property based on a Rental Yield</div>
  </div>
</section>

<!-- Step 4: forecast -->
<section class="panel" style="top:1488px;height:425px">
  <div class="stepper">
    <div class="step" style="left:33px"><div class="mark"><svg class="tick" viewBox="0 0 12 12"><path d="M2 6.5l2.6 2.6L10 3.5" fill="none" stroke="#0455a3" stroke-width="2"/></svg></div><span class="label">Property Type</span></div>
    <div class="step" style="left:219px"><div class="mark"><svg class="tick" viewBox="0 0 12 12"><path d="M2 6.5l2.6 2.6L10 3.5" fill="none" stroke="#0455a3" stroke-width="2"/></svg></div><span class="label">Property Location</span></div>
    <div class="step" style="left:413px"><div class="mark"><svg class="tick" viewBox="0 0 12 12"><path d="M2 6.5l2.6 2.6L10 3.5" fill="none" stroke="#0455a3" stroke-width="2"/></svg></div><span class="label">Property Valuation</span></div>
    <div class="step active" style="left:598px"><div class="mark"><span class="num">4</span></div><span class="label">Your Property Forecast</span></div>
    <div class="step" style="left:825px"><div class="mark"><span class="num">5</span></div><span class="label">Calculation</span></div>
  </div>
  <div class="question" style="top:84px">Your Property Price Forecast</div>
  <div class="btn prev" style="top:75px">PREVIOUS</div>
  <div class="btn next" style="top:75px">NEXT</div>
  <div class="line-text" style="left:289px;top:114px">You have chosen to forecast property prices using</div>
  <div class="select" style="left:536px;top:110px;width:125px">Gross Rental Yield<svg width="8" height="5" viewBox="0 0 8 5"><path d="M1 1l3 3 3-3" fill="none" stroke="#666"/></svg></div>
  <div class="line-text" style="left:180px;top:150px">You can see how this ratio has changed over time(in blue) below vs your assumption (in red) for</div>
  <div class="select" style="left:644px;top:146px;width:125px">Sydney House<svg width="8" height="5" viewBox="0 0 8 5"><path d="M1 1l3 3 3-3" fill="none" stroke="#666"/></svg></div>
  <svg style="position:absolute;left:318px;top:180px" width="315" height="177" viewBox="478 1668 315 177" font-family="Source Sans 3,Arial,sans-serif">
    <rect x="478.5" y="1668.5" width="314" height="176" fill="#fff" stroke="#ececec"/>
    <path d="M551 1687h14" stroke="#5aa9e6" stroke-width="1.5"/><text x="573" y="1690" font-size="9" fill="#666">Gross Rental Yield</text>
    <path d="M666 1687h14" stroke="#e2701f" stroke-width="1.5"/><text x="688" y="1690" font-size="9" fill="#666">forecast</text>
    <g stroke="#eeeeee"><path d="M500 1707h290M500 1727h290M500 1747h290M500 1768h290M500 1788h290M500 1808h290"/></g>
    <path d="M500 1829h290" stroke="#cccccc"/>
    <g font-size="6.5" fill="#666" text-anchor="end"><text x="496" y="1709">300K</text><text x="496" y="1729">250K</text><text x="496" y="1749">200K</text><text x="496" y="1770">150K</text><text x="496" y="1790">100K</text><text x="496" y="1810">50K</text><text x="496" y="1831">0</text></g>
    <g font-size="6.5" fill="#666" text-anchor="middle"><text x="513" y="1841">Jan</text><text x="538" y="1841">Feb</text><text x="562" y="1841">Mar</text><text x="586" y="1841">Apr</text><text x="610" y="1841">May</text><text x="634" y="1841">Jun</text><text x="657" y="1841">Jul</text><text x="681" y="1841">Aug</text><text x="705" y="1841">Sep</text><text x="729" y="1841">Oct</text><text x="753" y="1841">Nov</text><text x="777" y="1841">Dec</text></g>
    <path d="M513 1788L538 1782 562 1779 586 1769 610 1773 634 1767" fill="none" stroke="#5aa9e6" stroke-width="1.2"/>
    <path d="M634 1767Q705 1748 777 1719" fill="none" stroke="#e2701f" stroke-width="1.2" stroke-dasharray="3 2"/>
  </svg>
  <div class="question" style="top:368px;font-size:11.5px">By Default we assume the ratio stays at the latest value of 3.4%.You can Change this assumption using The Slider</div>
  <div class="track" style="left:203px;width:546px;top:393px"><div class="fill" style="width:83px"></div><div class="knob" style="left:83px"></div></div>
  <div class="question" style="top:402px;font-size:10.5px;color:#888">3.4%</div>
</section>

<!-- Step 5: calculation -->
<section class="panel" style="top:2008px;height:424px">
  <div class="stepper">
    <div class="step" style="left:33px"><div class="mark"><svg class="tick" viewBox="0 0 12 12"><path d="M2 6.5l2.6 2.6L10 3.5" fill="none" stroke="#0455a3" stroke-width="2"/></svg></div><span class="label">Property Type</span></div>
    <div class="step" style="left:219px"><div class="mark"><svg class="tick" viewBox="0 0 12 12"><path d="M2 6.5l2.6 2.6L10 3.5" fill="none" stroke="#0455a3" stroke-width="2"/></svg></div><span class="label">Property Location</span></div>
    <div class="step" style="left:413px"><div class="mark"><svg class="tick" viewBox="0 0 12 12"><path d="M2 6.5l2.6 2.6L10 3.5" fill="none" stroke="#0455a3" stroke-width="2"/></svg></div><span class="label">Property Valuation</span></div>
    <div class="step" style="left:598px"><div class="mark"><svg class="tick" viewBox="0 0 12 12"><path d="M2 6.5l2.6 2.6L10 3.5" fill="none" stroke="#0455a3" stroke-width="2"/></svg></div><span class="label">Your Property Forecast</span></div>
    <div class="step active" style="left:825px"><div class="mark"><span class="num">5</span></div><span class="label">Calculation</span></div>
  </div>
  <div class="btn prev" style="top:67px">PREVIOUS</div>
  <div class="btn next" style="top:67px">NEXT</div>

  <div class="card" style="left:9px;width:280px">
    <div class="line-text small" style="left:6px;top:14px">Choose Property :</div>
    <div class="select" style="left:96px;top:8px;width:166px;font-size:9.5px">Sydney House<svg width="8" height="5" viewBox="0 0 8 5"><path d="M1 1l3 3 3-3" fill="none" stroke="#666"/></svg></div>
    <div class="line-text small" style="left:6px;top:50px">Choose Alternative Investment :</div>
    <div class="select" style="left:163px;top:44px;width:99px;font-size:9.5px">Global Shares<svg width="8" height="5" viewBox="0 0 8 5"><path d="M1 1l3 3 3-3" fill="none" stroke="#666"/></svg></div>
    <div class="line-text small" style="left:6px;top:78px">How Much will the Property Cost?</div>
    <div class="line-text" style="right:8px;top:84px;font-size:9px;color:#555">$500,000</div>
    <div class="track" style="left:6px;width:266px;top:98px"><div class="fill" style="width:46px"></div><div class="knob" style="left:46px"></div></div>
    <div class="line-text small" style="left:6px;top:111px">How much will you invest?</div>
    <div class="line-text" style="right:8px;top:117px;font-size:9px;color:#555">$200,000</div>
    <div class="track" style="left:6px;width:266px;top:131px"><div class="fill" style="width:46px"></div><div class="knob" style="left:46px"></div></div>
  </div>

  <svg class="card" style="left:293px;width:267px" viewBox="453 2135 267 147" font-family="Source Sans 3,Arial,sans-serif">
    <text x="467" y="2151" font-size="6.5" fill="#333" font-weight="600">Share of Families with Student Loan Debt for Those Ages 25–55, 1989–2016</text>
    <g stroke="#eeeeee"><path d="M480 2160h218M480 2178h218M480 2196h218M480 2214h218M480 2232h218"/></g>
    <path d="M480 2250h218" stroke="#ccc"/>
    <g font-size="4" fill="#888"><text x="470" y="2162">40%</text><text x="470" y="2180">30%</text><text x="470" y="2198">20%</text><text x="470" y="2216">10%</text><text x="470" y="2234">5%</text></g>
    <g font-size="4" fill="#888" text-anchor="middle"><text x="489" y="2257">1989</text><text x="512" y="2257">1992</text><text x="535" y="2257">1995</text><text x="558" y="2257">1998</text><text x="580" y="2257">2001</text><text x="603" y="2257">2004</text><text x="626" y="2257">2007</text><text x="649" y="2257">2010</text><text x="672" y="2257">2013</text><text x="694" y="2257">2016</text></g>
    <path d="M484 2226L507 2232 530 2220 553 2226 576 2218 600 2212 623 2198 646 2190 670 2184 694 2174" fill="none" stroke="#e0399a" stroke-width="1"/>
    <path d="M484 2230L507 2224 530 2228 553 2222 576 2224 600 2218 623 2214 646 2208 670 2202 694 2194" fill="none" stroke="#3aa8de" stroke-width="1"/>
    <path d="M484 2234L507 2230 530 2232 553 2230 576 2228 600 2226 623 2222 646 2220 670 2220 694 2218" fill="none" stroke="#777" stroke-width="1"/>
    <g font-size="4.5" font-weight="600"><text x="670" y="2172" fill="#e0399a">BLACK</text><text x="670" y="2206" fill="#3aa8de">WHITE</text><text x="665" y="2228" fill="#555">HISPANIC</text></g>
    <g font-size="3.6" fill="#777"><text x="466" y="2268">Source: household finance survey, 1989–2016</text><text x="466" y="2273">Note: shares cover families with debt</text></g>
    <text x="710" y="2275" font-size="4" font-weight="700" fill="#1696d2" text-anchor="end">CIVIC DATA LAB</text>
  </svg>

  <svg class="card" style="left:563px;width:230px" viewBox="723 2135 230 147" font-family="Source Sans 3,Arial,sans-serif">
    <g font-size="4" fill="#777" text-anchor="middle"><text x="763" y="2150">-50%</text><text x="779" y="2150">-40%</text><text x="794" y="2150">-30%</text><text x="810" y="2150">-20%</text><text x="825" y="2150">-10%</text><text x="840" y="2150">0%</text><text x="855" y="2150">10%</text><text x="871" y="2150">20%</text><text x="886" y="2150">30%</text><text x="902" y="2150">40%</text><text x="917" y="2150">50%</text><text x="933" y="2150">60%</text><text x="946" y="2150">70%</text></g>
    <path d="M840 2155v95" stroke="#ddd"/>
    <g font-size="4.5" fill="#444"><text x="730" y="2165">Survey Item A</text><text x="730" y="2185">Survey Item B</text><text x="730" y="2205">Survey Item C</text><text x="730" y="2225">Survey Item D</text><text x="730" y="2245">Survey Item E</text></g>
    <g fill="#e03b4b"><rect x="830" y="2159" width="4" height="9"/><rect x="815" y="2179" width="8" height="9"/><rect x="810" y="2199" width="6" height="9"/><rect x="778" y="2219" width="10" height="9"/><rect x="776" y="2239" width="26" height="9"/></g>
    <g fill="#f07f8a"><rect x="834" y="2159" width="6" height="9"/><rect x="823" y="2179" width="17" height="9"/><rect x="816" y="2199" width="24" height="9"/><rect x="788" y="2219" width="52" height="9"/><rect x="802" y="2239" width="38" height="9"/></g>
    <g fill="#8cc2ea"><rect x="840" y="2159" width="26" height="9"/><rect x="840" y="2179" width="42" height="9"/><rect x="840" y="2199" width="26" height="9"/><rect x="840" y="2219" width="30" height="9"/><rect x="840" y="2239" width="22" height="9"/></g>
    <g fill="#4a8fd3"><rect x="866" y="2159" width="67" height="9"/><rect x="882" y="2179" width="31" height="9"/><rect x="866" y="2199" width="32" height="9"/><rect x="870" y="2219" width="32" height="9"/><rect x="862" y="2239" width="18" height="9"/></g>
    <g font-size="4" fill="#444" text-anchor="middle"><text x="788" y="2259">Strongly</text><text x="788" y="2264">Disagree</text><text x="822" y="2259">Disagree</text><text x="854" y="2259">Agree</text><text x="875" y="2259">Strongly</text><text x="875" y="2264">Agree</text></g>
  </svg>

  <div class="card result" style="left:796px;width:146px">
    <div class="head" style="margin-top:28px">After 5 Years:</div>
    <div class="sub" style="margin-top:2px">Shares will Return $82,431 more</div>
    <div class="head" style="margin-top:3px">After 10 Years:</div>
    <div class="sub" style="margin-top:3px;font-size:10.5px">$160,176</div>
    <div class="head" style="margin-top:9px">Debt Contribution</div>
  </div>

  <div class="note">Note : These are indicative figures based on a broad range of assumption (below).Please contact Ambertide Funds or a financial planner before making any investment based on the assumptions from this calculator.</div>
  <div class="advanced">&rsaquo;&nbsp; Advanced options</div>
</section>

</div>
</body>
</html>
```